Animal Eye Clinic needs a Business card

We are a new veterinary ophthalmology practice (Tessaly Animal Eye Care) and we need a business card designed. We only see animal eyes - we are not a regular veterinary clinic. We already have a logo. We are looking for a professional, good looking business card to hand out to our clients. We are looking for something simple but professional and contemporary. Our logo is likely the only picture/graphic that needs to be on the card.
Updates

Contact Information for Business Card

Marisol Dunkley, BSc, DVM, MSc, DipACVO
Veterinary Ophthalmologist

Phone: 250.418.3097
Email: tessalyanimaleyecare@mailbrook.net
Website: tessalyanimaleyecare.net
Address: 1840 Pellworth Rd
Kelowna, BC, V4T 8M3

Colors

Designer to choose colors to be used in the design.

Requirements
Must have
• Our logo (attached)

```html
<!DOCTYPE html>
<html lang="en">
<head>
<meta charset="utf-8">
<title>Tessaly Animal Eye Care – Business Card</title>
<link href="https://fonts.googleapis.com/css2?family=Roboto:wght@400;500;700&display=swap" rel="stylesheet">
<style>
  :root {
    --teal: #1b97a8;
    --charcoal: #2c2b2b;
    --grey: #757575;
    --text-grey: #5f5f5f;
    --paper: #ffffff;
    --backdrop: #d9dcdf;
  }
  * { box-sizing: border-box; margin: 0; padding: 0; }
  html, body {
    width: 1200px; height: 800px; overflow: hidden;
    background: var(--backdrop);
    font-family: "Roboto", Arial, sans-serif;
  }
  .sheet {
    position: relative; width: 1200px; height: 800px;
  }
  .card {
    position: absolute; width: 630px; height: 360px; overflow: hidden;
    box-shadow: 0 6px 18px rgba(0,0,0,0.18);
  }
  .card--back { left: 430px; top: 28px; background: var(--charcoal); }
  .card--front { left: 140px; top: 412px; background: var(--paper); }

  /* brand name block */
  .brand {
    display: flex; align-items: center; gap: 14px;
    color: var(--teal); font-weight: 700; letter-spacing: 0.5px;
  }
  .brand__dot {
    width: 34px; height: 34px; border-radius: 50%; background: var(--teal); flex: none;
  }
  .brand__name { font-size: 27px; line-height: 1; }

  /* back side */
  .back__art {
    position: absolute; left: 0; top: 0; width: 230px; height: 360px;
    background: linear-gradient(135deg, var(--teal) 0%, var(--teal) 62%, var(--grey) 62%, var(--grey) 100%);
    clip-path: polygon(0 0, 72% 0, 100% 10%, 92% 62%, 70% 76%, 50% 100%, 0 100%);
  }
  .back__brand { position: absolute; left: 268px; top: 148px; }
  .back__web {
    position: absolute; left: 318px; top: 268px;
    color: var(--teal); font-size: 17px; letter-spacing: 0.6px;
  }

  /* front side */
  .front__brand { position: absolute; left: 42px; top: 38px; }
  .front__brand .brand__name { font-size: 25px; }
  .person { position: absolute; left: 42px; top: 118px; }
  .person__name {
    color: var(--teal); font-weight: 700; font-size: 22px; letter-spacing: 0.3px;
  }
  .person__creds { font-size: 15px; font-weight: 700; }
  .person__title { color: var(--text-grey); font-size: 17px; margin-top: 3px; }
  .contact { position: absolute; left: 42px; top: 190px; list-style: none; }
  .contact__item {
    display: flex; align-items: center; gap: 8px;
    color: var(--text-grey); font-size: 17px; line-height: 23px;
  }
  .contact__icon { width: 14px; height: 14px; flex: none; fill: none; stroke: var(--teal); stroke-width: 1.6; }
  .contact__icon--solid { fill: var(--teal); stroke: none; }
  .address { position: absolute; left: 42px; top: 282px; color: var(--text-grey); font-size: 17px; }

  .front__art {
    position: absolute; left: 420px; top: 118px; width: 300px; height: 300px;
    border-radius: 50%; background: var(--teal);
  }
  .front__corner {
    position: absolute; right: 0; bottom: 0; width: 120px; height: 90px;
    background: var(--grey);
    clip-path: polygon(100% 0, 100% 100%, 0 100%);
  }
</style>
</head>
<body>
<main class="sheet">

  <section class="card card--back" aria-label="Card back">
    <div class="back__art" role="img" aria-label="Illustration of a horse and a cat in profile"></div>
    <div class="brand back__brand">
      <span class="brand__dot"></span>
      <span class="brand__name">Tessaly Animal Eye Care</span>
    </div>
    <p class="back__web">tessalyanimaleyecare.net</p>
  </section>

  <section class="card card--front" aria-label="Card front">
    <div class="brand front__brand">
      <span class="brand__dot"></span>
      <span class="brand__name">Tessaly Animal Eye Care</span>
    </div>

    <div class="person">
      <p class="person__name">MARISOL DUNKLEY, <span class="person__creds">BSc, DVM, MSc, DipACVO</span></p>
      <p class="person__title">Veterinary Ophthalmologist</p>
    </div>

    <ul class="contact">
      <li class="contact__item">
        <svg class="contact__icon contact__icon--solid" viewBox="0 0 16 16" aria-hidden="true"><path d="M3 1l3 3-1.5 2a9 9 0 0 0 5.5 5.5L12 10l3 3-2 2C7 15 1 9 1 3z"/></svg>
        250.418.3097
      </li>
      <li class="contact__item">
        <svg class="contact__icon" viewBox="0 0 16 16" aria-hidden="true"><rect x="1" y="3" width="14" height="10"/><path d="M1 3l7 6 7-6"/></svg>
        tessalyanimaleyecare@mailbrook.net
      </li>
      <li class="contact__item">
        <svg class="contact__icon" viewBox="0 0 16 16" aria-hidden="true"><circle cx="8" cy="8" r="6.5"/><ellipse cx="8" cy="8" rx="3" ry="6.5"/><path d="M1.5 8h13"/></svg>
        tessalyanimaleyecare.net
      </li>
    </ul>
    <p class="address">1840 Pellworth Rd, Kelowna, BC, V4T 8M3</p>

    <div class="front__art" role="img" aria-label="Illustration of a dog in profile inside a teal circle"></div>
    <div class="front__corner"></div>
  </section>

</main>
</body>
</html>
```